Memoir author looking for book cover design

Title:
"Rain, Rust and Return"

Subtitle:
"A Season Spent Chasing Our Father Across the Coastline"

My book is about the 18-month-long search and grieving process after my husband went missing from a hiking accident.
See "notesbeyondthequietharbor.example" for background

(An "ampersand" may look best, but I'm unable to enter it in this format)

Reason: Having difficulty finishing up, in part due to time difference. Don't want designers to have to work in the middle of the night!

```html
<!DOCTYPE html>
<html lang="en">
<head>
<meta charset="utf-8">
<title>Rain, Rust and Return — Book Cover</title>
<link rel="stylesheet" href="https://fonts.googleapis.com/css2?family=Arimo:wght@400&family=Aleo:wght@400&display=swap">
<style>
  :root {
    --page-bg: #efe9e2;
    --cover-top: #ece3e0;
    --cover-bottom: #e7dcd8;
    --title-red: #e8161c;
    --title-black: #0b0b0b;
    --subtitle-ink: #1a1a1a;
    --figure-dark: #4a2f27;
    --figure-mid: #7a5246;
    --figure-light: #b48c80;
  }
  * { margin: 0; padding: 0; box-sizing: border-box; }
  html, body {
    width: 1200px;
    height: 1200px;
    overflow: hidden;
    background: var(--page-bg);
  }
  .stage {
    position: relative;
    width: 1200px;
    height: 1200px;
  }
  .book-cover {
    position: absolute;
    left: 270px;
    top: 72px;
    width: 660px;
    height: 1056px;
    background: linear-gradient(180deg, var(--cover-top) 0%, var(--cover-bottom) 100%);
    overflow: hidden;
  }
  .title-word {
    position: absolute;
    font-family: "Arimo", Arial, sans-serif;
    font-weight: 400;
    line-height: 1;
    color: var(--title-black);
    white-space: nowrap;
  }
  .title-word--love {
    color: var(--title-red);
    left: 110px;
    top: 4px;
    font-size: 124px;
  }
  .title-word--loss {
    left: 200px;
    top: 96px;
    font-size: 136px;
  }
  .title-word--amp {
    left: 408px;
    top: 212px;
    font-size: 120px;
  }
  .title-word--return {
    right: 22px;
    top: 320px;
    font-size: 108px;
  }
  .cover-figure {
    position: absolute;
    left: 0;
    top: 460px;
    width: 240px;
    height: 596px;
    border-radius: 62% 38% 0 0 / 24% 20% 0 0;
    background: linear-gradient(160deg, var(--figure-mid) 0%, var(--figure-dark) 45%, var(--figure-mid) 75%, var(--figure-light) 100%);
  }
  .subtitle {
    position: absolute;
    left: 254px;
    width: 400px;
    top: 712px;
    font-family: "Aleo", Georgia, serif;
    font-size: 24px;
    line-height: 1.15;
    color: var(--subtitle-ink);
    text-align: center;
    white-space: nowrap;
  }
  .author-name {
    position: absolute;
    right: 18px;
    bottom: 14px;
    font-family: "Aleo", Georgia, serif;
    font-size: 38px;
    line-height: 1;
    color: var(--title-black);
    letter-spacing: 0.5px;
  }
</style>
</head>
<body>
  <main class="stage">
    <section class="book-cover">
      <h1 class="book-title">
        <span class="title-word title-word--love">RAIN</span>
        <span class="title-word title-word--loss">RUST</span>
        <span class="title-word title-word--amp">&amp;</span>
        <span class="title-word title-word--return">RETURN</span>
      </h1>
      <div class="cover-figure" role="img" aria-label="Illustration of a woman with long brown hair seen from behind, looking toward the horizon"></div>
      <p class="subtitle">A Season Spent Chasing Our Father<br>Across the Coastline</p>
      <p class="author-name">AUTHOR NAME</p>
    </section>
  </main>
</body>
</html>
```